Design my site www.briefmarkpost.com

So here is what I am thinking in terms of design:

https://plenvo.com

https://www.skylarkjetways.com

http://quillweekly.com/harbor-tower-plaza/

I want the theme to be white and blue (royal blue). I attached a paint picture of what I would like the site to look like in terms of placing the text. Generally, what I like about the sites above is that they are simple, you can navigate easily and have some kind of idea of what's going on by looking at the center (picture and motto). Let's establish a clear understanding of how the functional part of the site would look like. Please see the picture attached.

I want to keep it simple: On top would be the Name 'BRIEFMARK post", somewhere to the right on top on the page would be 'Sign in" button.

In the center would be a picture (maybe a video) with the Motto (on top of it all in capital) OBSERVE NAVIGATE DECIDE and below would be the "sign up now"

Below the picture (like on quillweekly.com site) or to the left on top of the page would be "About Us', "Press" "Contact Us' buttons.

Then once the user gets to his page his got 3 tabs " Press Headlines", "Events", " Briefings".

we would keep the same format I only have on the site, but separate for every Tab.

I do not want the user to get distracted. I also want him to be able to access the page though mobile phone and be able to get automatic updates just like Zentro Pings without having to sign in daily.

The landing page must be minimalist yet with business/corporate feel where users can navigate easily and a "what you see is what you get" approach. You want an image or video (personally I prefer the video.. it does capture the users attention instantly, as long as it is an interesting video), with your taglines in it.

Sections available to public: About Us, Contact Us, Landing Page with Signup Option

Private: Public Sections + User Account Page, Tabs for (Events, Press Headlines, Briefings)

Target Market(s)

PR/media monitoring/diplomatic community

Coding

Coded - Design and coding required

Number of Pages Required

1 page

Font styles to use
Serif
Sans Serif

Colors
0255a3
ec1f27

Requirements
Must have
• a simple landing page, that is user friendly.
Nice to have
• a video with the explanation of how to navigate the site
Should not have
• too many colors, graphs etc.

```html
<!DOCTYPE html>
<html lang="en">
<head>
<meta charset="utf-8">
<title>BRIEFMARK post</title>
<link rel="stylesheet" href="https://fonts.googleapis.com/css2?family=Roboto:wght@300;400;500;700&family=Great+Vibes&display=swap">
<style>
:root{
  --royal:#0255a3;
  --royal-dark:#01468a;
  --red:#ec1f27;
  --ink:#2b2f36;
  --muted:#6c727c;
  --soft:#f3f4f6;
  --line:#dfe3e8;
  --footer:#2c3036;
  --footer-deep:#24272c;
  --footer-text:#a9afb8;
  --white:#ffffff;
}
*{box-sizing:border-box;margin:0;padding:0}
html,body{width:778px;height:1200px;overflow:hidden}
body{font-family:"Roboto",Arial,sans-serif;color:var(--ink);background:var(--white);position:relative}

/* Header */
.site-header{height:40px;display:flex;align-items:center;justify-content:space-between;padding-left:31px;background:var(--white);box-shadow:0 1px 3px rgba(0,0,0,.08);position:relative;z-index:2}
.brand{font-weight:700;font-size:19px;color:var(--royal);letter-spacing:.5px}
.main-nav{display:flex;align-items:center;height:100%}
.main-nav a{font-size:8px;font-weight:500;color:var(--ink);text-decoration:none;margin-right:18px;letter-spacing:.3px}
.main-nav .sign-in{margin:0 26px 0 4px;height:100%;width:54px;background:var(--royal);color:var(--white);display:flex;align-items:center;justify-content:center}

/* Hero */
.hero{position:relative;height:430px;overflow:hidden}
.hero-visual{position:absolute;inset:0;background:linear-gradient(100deg,#b9aea4 0%,#d3cdc6 35%,#e4e2df 60%,#eeeeed 100%)}
.hero-copy{position:absolute;left:330px;top:178px;width:360px;text-align:center}
.hero-title{font-family:"Great Vibes",cursive;font-weight:400;font-size:52px;color:var(--white);text-shadow:0 1px 4px rgba(0,0,0,.25);line-height:1}
.hero-sub{margin-top:10px;font-size:13px;font-weight:500;color:var(--white);text-shadow:0 1px 3px rgba(0,0,0,.3)}
.hero-actions{margin-top:20px;display:flex;justify-content:center;gap:26px}
.btn{display:inline-flex;align-items:center;justify-content:center;height:18px;padding:0 12px;font-size:6.5px;font-weight:500;text-decoration:none;letter-spacing:.4px;border-radius:2px}
.btn-primary{background:var(--royal);color:var(--white)}
.btn-outline{border:1px solid var(--white);color:var(--white)}
.hero-signup{position:absolute;left:346px;top:364px;width:86px;height:24px;background:var(--white);color:var(--red);font-size:7px;font-weight:700;display:flex;align-items:center;justify-content:center;text-decoration:none;letter-spacing:.4px;border-radius:2px}

/* Section titles */
.section-title{text-align:center;color:var(--royal);font-size:16px;font-weight:500}
.section-title::after{content:"";display:block;width:38px;height:2px;background:var(--royal);margin:8px auto 0}

/* Headlines */
.headlines{height:263px;background:var(--soft);padding-top:36px}
.feature-grid{display:flex;justify-content:space-between;padding:0 30px;margin-top:26px}
.feature{width:226px;text-align:center}
.feature-icon{width:44px;height:44px;background:var(--royal);margin:0 auto;display:flex;align-items:center;justify-content:center}
.feature h3{font-size:12px;font-weight:500;margin-top:10px;color:var(--ink)}
.feature p{font-size:7.5px;line-height:1.55;color:var(--muted);margin-top:7px}

/* Process */
.process{height:242px;padding-top:18px;position:relative}
.process-track{position:absolute;left:117px;right:116px;top:102px;height:1px;background:var(--line)}
.steps{display:flex;justify-content:space-between;padding:0 40px;margin-top:44px;position:relative}
.step{width:160px;text-align:center}
.step-icon{width:54px;height:54px;border-radius:50%;background:var(--royal);margin:0 auto;display:flex;align-items:center;justify-content:center;box-shadow:0 0 0 5px var(--white),0 0 0 6px var(--line)}
.step h4{font-size:11px;font-weight:500;margin-top:20px;color:var(--ink)}

/* Footer */
.site-footer{height:200px;background:var(--footer);color:var(--footer-text);display:flex;padding:16px 31px 0;gap:22px}
.footer-col{width:162px;font-size:6.5px;line-height:1.6}
.footer-col h5{color:var(--white);font-size:9px;font-weight:500;margin-bottom:10px}
.footer-col p{margin-bottom:6px}
.footer-col strong{color:var(--white);font-weight:500}
.socials{display:flex;gap:6px;margin-top:8px}
.socials span{width:10px;height:10px;border-radius:50%;background:var(--footer-text)}
.post{display:flex;gap:8px;margin-bottom:9px;align-items:center}
.post-thumb{width:26px;height:20px;background:linear-gradient(135deg,#8b8f96,#5d6168);flex:none}
.post-title{color:var(--white);font-size:7px}
.post-date{font-size:6px}
.quote-mark{font-family:Georgia,serif;font-size:26px;line-height:.7;color:var(--footer-text);float:left;margin-right:6px}
.reviewer{display:flex;align-items:center;gap:8px;margin-top:10px;clear:both}
.reviewer-photo{width:30px;height:30px;border-radius:50%;background:linear-gradient(135deg,#9aa0a8,#6b7078)}
.reviewer-name{color:var(--white);font-size:8px}
.copyright{height:25px;background:var(--footer-deep);color:var(--footer-text);font-size:6.5px;display:flex;align-items:center;padding-left:31px}
</style>
</head>
<body>

<header class="site-header">
  <div class="brand">BRIEFMARK post</div>
  <nav class="main-nav">
    <a href="#">ABOUT US</a>
    <a href="#">CONTACT US</a>
    <a href="#" class="sign-in">SIGN IN</a>
  </nav>
</header>

<section class="hero">
  <div class="hero-visual" role="img" aria-label="Photo of a cheerful woman celebrating with raised fists on a light background"></div>
  <div class="hero-copy">
    <h1 class="hero-title">Ready to Enjoy?</h1>
    <p class="hero-sub">Grab This Perfect BRIEFMARK post Now</p>
    <div class="hero-actions">
      <a href="#" class="btn btn-primary">SIGN UP NOW</a>
      <a href="#" class="btn btn-outline">LEARN MORE</a>
    </div>
  </div>
  <a href="#" class="hero-signup">SIGN UP NOW</a>
</section>

<section class="headlines">
  <h2 class="section-title">Headlines</h2>
  <div class="feature-grid">
    <article class="feature">
      <div class="feature-icon">
        <svg width="22" height="22" viewBox="0 0 24 24" fill="none" stroke="#fff" stroke-width="1.8"><rect x="5" y="3" width="14" height="18"/><path d="M9 7h2M13 7h2M9 11h2M13 11h2M9 15h2M13 15h2M11 21v-3h2v3"/></svg>
      </div>
      <h3>About Us</h3>
      <p>We gather daily press coverage, event notes and diplomatic briefings into one calm place, so your team can read what matters, follow key stories and act with confidence every morning.</p>
    </article>
    <article class="feature">
      <div class="feature-icon">
        <svg width="22" height="22" viewBox="0 0 24 24" fill="none" stroke="#fff" stroke-width="1.8"><circle cx="12" cy="6" r="3"/><path d="M7 21v-7a5 5 0 0 1 10 0v7M12 14v7"/></svg>
      </div>
      <h3>Press</h3>
      <p>Our editors scan hundreds of outlets around the clock, picking the headlines that shape policy and markets, then sending them to you as short, clear summaries you can share.</p>
    </article>
    <article class="feature">
      <div class="feature-icon">
        <svg width="22" height="22" viewBox="0 0 24 24" fill="none" stroke="#fff" stroke-width="1.8"><rect x="7" y="2" width="10" height="20" rx="2"/><path d="M11 18h2"/></svg>
      </div>
      <h3>Contact Us</h3>
      <p>Questions about plans, alerts or team access? Write to our support desk any day of the week and a member of our staff will reply within a few working hours to help.</p>
    </article>
  </div>
</section>

<section class="process">
  <h2 class="section-title">Our Process</h2>
  <div class="process-track"></div>
  <div class="steps">
    <div class="step">
      <div class="step-icon"><svg width="22" height="22" viewBox="0 0 24 24" fill="none" stroke="#fff" stroke-width="2"><circle cx="12" cy="8" r="4"/><path d="M4 21a8 8 0 0 1 16 0"/></svg></div>
      <h4>1. Become a Member</h4>
    </div>
    <div class="step">
      <div class="step-icon"><svg width="22" height="22" viewBox="0 0 24 24" fill="none" stroke="#fff" stroke-width="2"><path d="M3 5h7a2 2 0 0 1 2 2v13a2 2 0 0 0-2-2H3zM21 5h-7a2 2 0 0 0-2 2v13a2 2 0 0 1 2-2h7z"/></svg></div>
      <h4>2. Read By Doing</h4>
    </div>
    <div class="step">
      <div class="step-icon"><svg width="22" height="22" viewBox="0 0 24 24" fill="none" stroke="#fff" stroke-width="2" stroke-linejoin="round"><path d="M12 3l2.8 5.8 6.2.9-4.5 4.4 1 6.2L12 17.4l-5.5 2.9 1-6.2L3 9.7l6.2-.9z"/></svg></div>
      <h4>3. Engage with a Community</h4>
    </div>
    <div class="step">
      <div class="step-icon"><svg width="22" height="22" viewBox="0 0 24 24" fill="none" stroke="#fff" stroke-width="2" stroke-linejoin="round"><path d="M7 11v9H3v-9zM7 11l4-8a2 2 0 0 1 2 2v4h6a2 2 0 0 1 2 2l-2 7a2 2 0 0 1-2 2H7"/></svg></div>
      <h4>4. Take a Events</h4>
    </div>
  </div>
</section>

<footer class="site-footer">
  <div class="footer-col">
    <h5>Contacts</h5>
    <p>Reach our team for plans, press alerts and account help. We answer within one working day.</p>
    <p><strong>Phone:</strong> +1 (555) 014 2290</p>
    <p><strong>Office:</strong> 218 Orchard Lane, Fairview</p>
    <p><strong>Email:</strong> hello@briefmarkpost.com</p>
    <div class="socials"><span></span><span></span><span></span><span></span></div>
  </div>
  <div class="footer-col">
    <h5>Recent Posts</h5>
    <div class="post"><div class="post-thumb" role="img" aria-label="Post thumbnail photo"></div><div><div class="post-title">Standard Post</div><div class="post-date">Jun 05, 2015 · 2 comments</div></div></div>
    <div class="post"><div class="post-thumb" role="img" aria-label="Post thumbnail photo"></div><div><div class="post-title">Video Post</div><div class="post-date">Jun 05, 2015 · 2 comments</div></div></div>
    <div class="post"><div class="post-thumb" role="img" aria-label="Post thumbnail photo"></div><div><div class="post-title">Post with Image</div><div class="post-date">Jun 05, 2015 · 2 comments</div></div></div>
  </div>
  <div class="footer-col">
    <h5>About Team</h5>
    <p>Our small team of analysts and editors has years of work in media, policy and public relations, reading the news so you can focus on decisions.</p>
    <p>Each briefing is checked by two people before it reaches you, keeping every summary short, fair and accurate.</p>
  </div>
  <div class="footer-col">
    <h5>Last Review</h5>
    <p><span class="quote-mark">“</span>The morning digest saves me an hour each day and keeps our whole office on the same page about the stories that matter most.</p>
    <div class="reviewer"><div class="reviewer-photo" role="img" aria-label="Reviewer portrait"></div><div><div class="reviewer-name">Owen Marsh</div><div>Reviewer</div></div></div>
  </div>
</footer>
<div class="copyright">Copyright © 2015. All Rights Reserved</div>

</body>
</html>
```